Business Card Design Project - bel soravin group

dear Sirs

we need business card design for our group ( BEL Soravin Group ) , i have got the Logo design of our group from pixel harbor in previous , so all need details relating to our group i think available with you, as well as the the chosen logo design

we hope to provide us with business card logo that to be appropaite and satisfactory to us .

thanks

note : logo design of our group is attached .
Updates

Reason: please extend the deadline of my project for additional 15 days because i didn't received appropriate design for our gruop yet . kindly beaware that i have received 77 design till now , supossed to send me 200-250 design at least . thanks

Target Market(s)

contents
-

name : Korvan EL Mistrani

position : Operation Manager

Industry/Entity Type

Business

Requirements
Must have

• person name

group logo
Nice to have
• logo color matching with back background

```html
<!DOCTYPE html>
<html lang="en">
<head>
<meta charset="utf-8">
<title>BEL Soravin Group – Business Card</title>
<link rel="stylesheet" href="https://fonts.googleapis.com/css2?family=Jost:wght@400;500&display=swap">
<style>
  :root {
    --backdrop: #8a8b87;
    --brand-blue: #0b4a86;
    --brand-blue-dark: #083a6b;
    --gold: #d9c58a;
    --gold-light: #ece0b4;
    --paper: #f4f6f8;
    --white: #ffffff;
  }
  * { margin: 0; padding: 0; box-sizing: border-box; }
  html, body { width: 1200px; height: 792px; overflow: hidden; }
  body {
    background: var(--backdrop);
    font-family: "Jost", sans-serif;
    position: relative;
  }
  .card {
    position: absolute;
    width: 540px;
    height: 309px;
    border-radius: 3px;
    overflow: hidden;
  }
  /* Front */
  .card-front { left: 50px; top: 110px; background: var(--brand-blue); color: var(--white); }
  .front-logo {
    position: absolute; right: 30px; top: 26px;
    display: flex; align-items: center; gap: 10px;
  }
  .logo-square { width: 16px; height: 16px; background: currentColor; }
  .logo-name { font-size: 21px; font-weight: 500; letter-spacing: 1px; text-transform: uppercase; }
  .name-band {
    position: absolute; left: 0; top: 168px; width: 92%; height: 34px;
    background: linear-gradient(90deg, var(--gold-light) 0%, var(--gold) 65%, rgba(217,197,138,0) 100%);
    display: flex; align-items: center; padding-left: 32px; gap: 14px;
    color: var(--brand-blue-dark);
  }
  .person-name { font-size: 20px; }
  .person-role { font-size: 14px; }
  .contact {
    position: absolute; top: 218px;
    display: grid; grid-template-columns: auto auto; column-gap: 6px; row-gap: 2px;
    font-size: 13.5px;
  }
  .contact-phones { left: 32px; }
  .contact-web { left: 268px; }
  .contact dt { color: var(--gold); text-align: right; }
  .contact dd { color: var(--white); }
  /* Back */
  .card-back {
    left: 610px; top: 372px; background: var(--paper); color: var(--brand-blue);
    border-right: 14px solid var(--brand-blue);
    display: flex; align-items: center; justify-content: center;
  }
  .back-logo { display: flex; align-items: center; gap: 16px; }
  .back-logo .logo-square { width: 30px; height: 30px; }
  .back-logo .logo-name { font-size: 38px; letter-spacing: 2px; }
</style>
</head>
<body>
  <section class="card card-front" aria-label="Business card front">
    <div class="front-logo">
      <span class="logo-square"></span>
      <span class="logo-name">BEL Soravin Group</span>
    </div>
    <div class="name-band">
      <span class="person-name">Korvan EL Mistrani</span>
      <span class="person-role">| Operation Manager</span>
    </div>
    <dl class="contact contact-phones">
      <dt>Tel :</dt><dd>+00 123 456 789</dd>
      <dt>Fax :</dt><dd>+00 123 456 789</dd>
      <dt>Mob :</dt><dd>+00 123 456 789</dd>
    </dl>
    <dl class="contact contact-web">
      <dt>Email :</dt><dd>korvan@belsoravingroup.com</dd>
      <dt>Website :</dt><dd>belsoravingroup.com</dd>
      <dt>PO. Box :</dt><dd>Your PO Box Number</dd>
    </dl>
  </section>

  <section class="card card-back" aria-label="Business card back">
    <div class="back-logo">
      <span class="logo-square"></span>
      <span class="logo-name">BEL SORAVIN GROUP</span>
    </div>
  </section>
</body>
</html>
```